Thornbury Cleaning – Website Redesign (Clean, Modern, Trust-Focused)

Thornbury Cleaning — Homepage Redesign Brief

Project Goal

We need a complete redesign of the homepage for our cleaning business, Thornbury Cleaning.
The goal is a clean, modern, trust-building homepage that works equally well for:
• Residential clients
• Commercial clients

The page should feel polished, reliable, easy to navigate, and completely free from clutter, gimmicks, or corporate-sounding fluff.

About Us (Context)

Thornbury Cleaning has operated in Sale, Victoria for over 30 years.
Our brand is built on:
• Reliability
• Convenience
• Long-term trust
• Straightforward, no-nonsense communication

We do not want to look like a large franchise, and we do not want to look cute or playful.
The design must feel modern, practical, confident, and professional.

What We Need Designed — Homepage Only

1. Hero Section

A clean, modern hero area with:
• A simple image or clean background (no clutter, no heavy overlays).
Images from our current site may be helpful, or you may source alternatives.
• Headline suggestion (designer may refine):
“30+ Years of Commercial and Residential Cleaning in Sale”
• Sub-headline suggestion:
“Trusted by locals for three decades.”
• Primary CTA button: Get a Quote

2. Trust-Building Logos

Positioned directly beneath the hero:
• Small, neat logos of organisations we work with
(RLK, Bramwell, Eastvale Regional Care, OPM, etc.)
• A clean Starlist Reviews block (stars + review count)
• Must be compact, tidy, evenly spaced — not loud or oversized

3. Trust Block / Problem–Solution Copy

This section introduces why hiring cleaners can be stressful and why reliability matters.

Headline example:
“Call the cleaners you can count on.”

We have existing copy for this section.
Please present it in a minimal, breathable, modern layout that is easy to scan.

4. Stats / Counters Section

Three sharp, structured stat boxes:
• 92+ Recurring Clients
• 4,150+ Visits Per Year
• 265+ Pre-Sale / Exit Cleans

These should look clean and understated — not oversized or gimmicky.

5. Values Section

A short section featuring our core values:
• Be Real
• Do It Right
• Have Fun
• Make It Easy

Designer has flexibility with layout.
(Sections 5 and 6 may swap depending on what flows better.)

6. Services Preview

A simple grid or row with links to our main services:
• Commercial Cleaning
• Residential Cleaning
• Window Cleaning
• Steam Cleaning

Small icons or photos are fine — but no clip art or cartoon-style graphics.

7. Footer

A very clean, simple footer with contact details.
No clutter, no heavy visual styling.

Style Requirements

Overall Tone
• Clean
• Modern
• Minimal
• Trust-driven
• Easy to read and navigate

Do NOT use
• Clip art
• Cute or playful icons
• Flowers, sparkles, “feminine” cleaning imagery
• Heavy or overly bold corporate fonts
• Busy backgrounds
• Long paragraphs of text

Reference Material

Current Website (for copy + structure only)

https://thornburycleaning-example.com.au

Rough Canva Mock-Up (layout inspiration only)

(We will upload this separately. It’s not a final design — just a loose concept for spacing/flow.)

Logo

Please use the new Thornbury Cleaning logo (uploaded in files) or a placeholder if needed. Attached is a potential for a new logo or site colours not wedded to the idea though.

What the Homepage Should Communicate

Within seconds, a visitor should understand that:
• We are established
• We are local
• We are reliable
• We make cleaning easy
• Getting a quote is quick and simple

The homepage should feel effortless, trustworthy, and modern.

Deliverable

A complete homepage design layout suitable for WordPress.
Figma, Adobe XD, or a similar design tool is fine.

Target Market(s)

Residential and commercial clients in Sale, Victoria and surrounding Gippsland region. Typical clients include busy households, office managers, receptionists, medical centres, community organisations, local businesses, and real estate/property professionals. Clients value reliability, simplicity, and stress-free long-term cleaning support.

Industry/Entity Type

Cleaning services (Residential & Commercial)

Font styles to use
Sans Serif

Requirements
Must have
• • Clean, modern, minimal layout • A trust-driven design that highlights proof (logos, stats, reviews) near the top • Clear hierarchy and no clutter • A strong hero section with simple messaging and a clear CTA • Trust logos + Starlist Reviews block directly under the hero • Structured stats/counters section • Values section (Be Real, Do It Right, Have Fun, Make It Easy) • Services preview (Commercial, Residential, Window, Steam/Carpet) • Clean footer with contact details • Use our new Thornbury Cleaning logo (or placeholder if needed) • Easy-to-read typography and spacing • Must feel like a local, real cleaning business — not a franchise
Nice to have
• • An option with centred hero text and an option with left-aligned text • Option to preview hero section with or without a quote form • Subtle use of the navy + gold palette (not heavy or corporate) • Soft, minimal background images (not busy city skylines) • Subtle section dividers or whitespace breaks to improve flow • Slightly rounded card corners for a friendly but still modern feel
Should not have
• • No clip-art, cartoon mops, sparkles, bubbles, or generic cleaning icons • No overly bold, blocky, or corporate fonts • No “mega-city” skylines (we are a regional/rural business) • No heavy overlays, dark gradients, or cluttered hero images • No long paragraphs or dense text blocks • No template-style designs that look generic or AI-generated • No overly feminine, overly masculine, or overly playful designs • No neon colors or high-saturation palettes

```html
<!DOCTYPE html>
<html lang="en">
<head>
<meta charset="utf-8">
<title>Thornbury Cleaning – Commercial and Residential Cleaning in Sale</title>
<link rel="stylesheet" href="https://fonts.googleapis.com/css2?family=Barlow+Condensed:wght@600;700;800&family=Inter:wght@400;500;600;700&display=swap">
<style>
:root{
  --navy:#0a4ea3;
  --blue:#0653ad;
  --ink:#0b1f3a;
  --gold:#f7c400;
  --cream:#fdf3c8;
  --pale:#e7eef8;
  --mist:#eef3fa;
  --line:#d6e0ee;
  --faint:#d2dbe7;
  --white:#ffffff;
  --text:#1e2a3c;
  --soft-blue:#3f7fd6;
}
*{box-sizing:border-box;margin:0;padding:0}
html,body{width:1200px;height:3233px;overflow:hidden}
body{font-family:"Inter",sans-serif;color:var(--text);background:var(--white);position:relative}
.display{font-family:"Barlow Condensed",sans-serif;font-weight:700;letter-spacing:-0.01em}
.gold{color:var(--gold)}
.navy{color:var(--navy)}
.btn{position:absolute;display:flex;align-items:center;justify-content:center;gap:8px;border-radius:20px;font-size:10.5px;font-weight:600;text-decoration:none;color:var(--white);background:var(--navy)}
.btn.yellow{background:var(--gold);color:var(--ink)}
.btn svg{width:10px;height:10px}

/* header */
.site-header{position:absolute;left:0;top:0;width:1200px;height:62px;background:var(--white)}
.wordmark{position:absolute;display:flex;align-items:center;gap:8px;font-family:"Inter",sans-serif;font-weight:700;white-space:nowrap}
.wordmark i{display:block;background:var(--gold)}
.header-mark{left:105px;top:21px;font-size:17px;color:var(--navy)}
.header-mark i{width:12px;height:12px}
.nav{position:absolute;left:312px;top:25px;display:flex;gap:22px;font-size:10px;font-weight:500;color:var(--ink)}
.nav .current{color:var(--navy)}
.help{position:absolute;display:flex;align-items:center;gap:8px}
.help svg{width:22px;height:22px}
.help small{display:block;font-size:8px;font-weight:600;color:var(--ink)}
.help strong{display:block;font-family:"Barlow Condensed",sans-serif;font-size:17px;font-weight:700;color:var(--ink);line-height:1}

/* hero */
.hero{position:absolute;left:0;top:62px;width:1200px;height:532px;background:linear-gradient(180deg,#3c332c 0%,#5a4a3d 40%,#3b2f27 75%,#221b16 100%)}
.hero-title{position:absolute;left:0;top:160px;width:1200px;text-align:center;color:var(--white);font-size:50px;line-height:58px}
.hero-sub{position:absolute;left:0;top:290px;width:1200px;text-align:center;color:var(--white);font-size:21px;font-weight:500}

/* trust band */
.trust{position:absolute;left:0;top:594px;width:1200px;height:94px;background:var(--pale)}
.trust-item{position:absolute;display:flex;align-items:center;gap:8px;font-weight:700;color:#55617a}
.trust-item .mark{width:14px;height:14px;background:#9aa6b9}
.rating{position:absolute;left:908px;top:22px;display:flex;align-items:center;gap:12px}
.rating .score{font-family:"Barlow Condensed",sans-serif;font-size:28px;font-weight:700;color:var(--navy)}
.rating .rule{width:1px;height:50px;background:#9aa6b9}
.rating .name{font-size:28px;font-weight:600;color:#4b5870;line-height:1}
.rating .rev{font-size:13px;color:#4b5870;font-weight:500}
.rating .rev span{color:var(--gold);letter-spacing:1px}

/* count on */
.count-title{position:absolute;left:0;top:760px;width:1200px;text-align:center;font-size:42px;color:var(--ink)}
.intro{position:absolute;left:150px;top:834px;width:900px;text-align:center;font-size:12px;line-height:22.5px;color:var(--ink)}
.intro p+p{margin-top:12px}
.stat{position:absolute;top:989px;width:250px;height:137px;border:1px solid var(--line);background:linear-gradient(180deg,#ffffff 0%,#eaf1fa 100%);text-align:center}
.stat b{display:block;margin-top:26px;font-family:"Barlow Condensed",sans-serif;font-size:40px;font-weight:700;color:var(--navy);line-height:1}
.stat span{display:block;margin-top:14px;font-family:"Barlow Condensed",sans-serif;font-size:23px;font-weight:600;color:var(--ink)}

/* values */
.values{position:absolute;left:0;top:1263px;width:1200px;height:781px;background:var(--blue)}
.eyebrow{position:absolute;left:0;top:77px;width:1200px;text-align:center;font-size:9.5px;font-weight:700;color:var(--white)}
.values-title{position:absolute;left:0;top:108px;width:1200px;text-align:center;font-size:42px;line-height:49px;color:var(--white)}
.values-photo{position:absolute;left:200px;top:256px;width:375px;height:387px;border-radius:4px;background:linear-gradient(160deg,#d7d8da 0%,#a9abae 45%,#4a4a4c 100%)}
.value{position:absolute;left:625px;width:380px;height:70px}
.value .ico{position:absolute;left:0;top:0;width:50px;height:50px;border-radius:50%;background:var(--cream);display:flex;align-items:center;justify-content:center}
.value .ico svg{width:26px;height:26px}
.value h3{position:absolute;left:62px;top:2px;font-family:"Barlow Condensed",sans-serif;font-size:19px;font-weight:700;color:var(--white)}
.value p{position:absolute;left:62px;top:28px;width:300px;font-size:8.8px;line-height:15px;color:#dfe8f6}

/* services */
.services{position:absolute;left:0;top:2044px;width:1200px;height:707px;background:var(--mist)}
.services-title{position:absolute;left:0;top:74px;width:1200px;text-align:center;font-size:42px;line-height:48px;color:var(--ink)}
.services-intro{position:absolute;left:0;top:190px;width:1200px;text-align:center;font-size:12px;line-height:19px;color:var(--ink)}
.card{position:absolute;top:277px;width:228px;height:165px;background:var(--white);border-radius:6px}
.card h3{position:absolute;left:18px;top:20px;font-family:"Barlow Condensed",sans-serif;font-size:21px;line-height:24px;font-weight:700;color:var(--ink)}
.card .ico{position:absolute;right:18px;top:20px;width:50px;height:50px;border-radius:50%;background:var(--navy);display:flex;align-items:center;justify-content:center}
.card .ico svg{width:26px;height:26px}
.card p{position:absolute;left:18px;top:92px;width:196px;font-size:9px;line-height:15px;color:var(--ink)}
.card .go{position:absolute;right:-6px;bottom:-6px;width:38px;height:38px;border-radius:50%;background:var(--white);border:5px solid var(--mist);display:flex;align-items:center;justify-content:center}
.card .go svg{width:12px;height:12px}
.marquee{position:absolute;left:0;top:2561px;width:1200px;height:60px;white-space:nowrap;font-family:"Barlow Condensed",sans-serif;font-size:52px;font-weight:800;color:var(--faint);display:flex;align-items:center;justify-content:space-between;padding-right:6px}

/* newsletter + footer */
.site-footer{position:absolute;left:0;top:2751px;width:1200px;height:482px;background:linear-gradient(180deg,#142a52 0%,#0b1d3d 60%,#08162f 100%)}
.newsletter{position:absolute;left:200px;top:2624px;width:800px;height:250px;background:var(--blue)}
.newsletter h2{position:absolute;left:0;top:44px;width:800px;text-align:center;font-size:40px;line-height:49px;color:var(--white)}
.newsletter .field{position:absolute;left:188px;top:174px;width:312px;height:30px;border-radius:15px;background:var(--white);font-size:9.5px;color:var(--ink);padding:9px 16px}
.footer-mark{left:200px;top:2960px;font-size:22px;color:var(--soft-blue)}
.footer-mark i{width:16px;height:16px}
.foot-about{position:absolute;left:200px;top:3017px;width:250px;font-size:9.3px;line-height:15px;color:#dfe6f2}
.foot-h{position:absolute;top:2954px;font-family:"Barlow Condensed",sans-serif;font-size:21px;font-weight:700;color:var(--white)}
.foot-line{position:absolute;display:flex;align-items:flex-start;gap:10px;font-size:9.5px;color:var(--white);line-height:15px}
.foot-line svg{width:11px;height:11px;flex:none;margin-top:2px}
.links{position:absolute;left:725px;top:2998px;font-size:9.5px;line-height:18.8px;color:var(--white);list-style:none}
.hours{position:absolute;left:868px;top:2998px;font-size:9.5px;line-height:18.8px;color:var(--white);font-weight:600}
.social{position:absolute;left:869px;top:3066px;width:30px;height:30px;border-radius:50%;border:1px solid var(--gold)}
.social i{position:absolute;left:11px;top:11px;width:6px;height:6px;border-radius:50%;background:var(--gold)}
.foot-rule{position:absolute;left:200px;top:3158px;width:800px;height:1px;background:#2c3f63}
.legal{position:absolute;top:3196px;font-size:9.5px;color:var(--white)}
.legal b{color:var(--gold);font-weight:600}
.cards{position:absolute;left:848px;top:3188px;display:flex;gap:4px}
.cards span{width:27px;height:18px;border-radius:3px;background:var(--white)}
</style>
</head>
<body>

<header class="site-header">
  <div class="wordmark header-mark"><i></i>Thornbury Cleaning</div>
  <nav class="nav">
    <span class="current">Home</span><span>Commercial</span><span>Residential</span><span>Window Cleaning</span><span>Steam Cleaning</span><span>Areas</span><span>Contact Us</span>
  </nav>
  <div class="help" style="left:836px;top:16px">
    <svg viewBox="0 0 24 24" fill="none" stroke="#0a4ea3" stroke-width="1.6"><path d="M5 4l3 1 1 4-2 1a11 11 0 0 0 6 6l1-2 4 1 1 3-2 2C10 20 3 13 3 6z"/><circle cx="17" cy="6" r="4" fill="#f7c400" stroke="none"/></svg>
    <div><small>Need Help?</small><strong>0412 555 019</strong></div>
  </div>
  <a class="btn" style="left:966px;top:16px;width:128px;height:30px" href="#quote">
    <svg viewBox="0 0 10 10" fill="#fff"><path d="M5 0l1 4 4 1-4 1-1 4-1-4-4-1 4-1z"/></svg>Get A Quote<svg viewBox="0 0 10 10" fill="#fff"><path d="M5 0l1 4 4 1-4 1-1 4-1-4-4-1 4-1z"/></svg>
  </a>
</header>

<section class="hero" role="img" aria-label="Photo of a tidy, warmly lit open-plan dining and living room">
  <h1 class="hero-title display"><span class="gold">30+ Years</span> of Commercial<br>and Residential <span class="gold">Cleaning in Sale</span></h1>
  <p class="hero-sub">Trusted by Locals For Three Decades.</p>
  <a class="btn" style="left:536px;top:343px;width:126px;height:30px" href="#quote">
    <svg viewBox="0 0 10 10" fill="#fff"><path d="M5 0l1 4 4 1-4 1-1 4-1-4-4-1 4-1z"/></svg>Get A Quote<svg viewBox="0 0 10 10" fill="#fff"><path d="M5 0l1 4 4 1-4 1-1 4-1-4-4-1 4-1z"/></svg>
  </a>
</section>

<section class="trust" aria-label="Organisations we work with">
  <div class="trust-item" style="left:105px;top:36px;font-size:20px"><span class="mark"></span>RLK</div>
  <div class="trust-item" style="left:262px;top:36px;font-size:20px">Bramwell</div>
  <div class="trust-item" style="left:462px;top:30px;font-size:13px;line-height:16px"><span class="mark" style="border-radius:50%"></span>Eastvale<br>Regional Care</div>
  <div class="trust-item" style="left:720px;top:36px;font-size:20px">OPM</div>
  <div class="rating">
    <div class="score">4.7</div><div class="rule"></div>
    <div><div class="name">Starlist</div><div class="rev">Reviews <span>★★★★★</span></div></div>
  </div>
</section>

<h2 class="count-title display"><span class="navy">Call The Cleaners</span> You Can Count on.</h2>
<div class="intro">
  <p>When you need help cleaning, the last thing you want is more stress.<br><b>Too often,</b> that’s exactly what happens — Cleaners don’t show up. Jobs get rushed or half-done.<br>And you’re left <b>wondering why you didn’t just do it yourself.</b></p>
  <p>You shouldn’t have to second-guess whether the job will be done right. You should be able to <b>book it, forget it, and trust it’s sorted — properly.</b><br><b>Trusted by locals for 30+ years</b> to deliver reliable, long-term cleaning — the kind you never have to second-guess.</p>
</div>
<div class="stat" style="left:200px"><b>92+</b><span>Recurring Clients</span></div>
<div class="stat" style="left:475px"><b>4,150+</b><span>Visits Per Year</span></div>
<div class="stat" style="left:750px"><b>265+</b><span>Pre-Sale / Exit Cleans</span></div>
<div class="help" style="left:466px;top:1158px">
  <svg viewBox="0 0 24 24" fill="none" stroke="#0a4ea3" stroke-width="1.6"><path d="M5 4l3 1 1 4-2 1a11 11 0 0 0 6 6l1-2 4 1 1 3-2 2C10 20 3 13 3 6z"/><circle cx="17" cy="6" r="4" fill="#f7c400" stroke="none"/></svg>
  <div><small>Need Help?</small><strong>0412 555 019</strong></div>
</div>
<a class="btn" style="left:604px;top:1158px;width:127px;height:30px" href="#quote">
  <svg viewBox="0 0 10 10" fill="#fff"><path d="M5 0l1 4 4 1-4 1-1 4-1-4-4-1 4-1z"/></svg>Get A Quote<svg viewBox="0 0 10 10" fill="#fff"><path d="M5 0l1 4 4 1-4 1-1 4-1-4-4-1 4-1z"/></svg>
</a>

<section class="values">
  <p class="eyebrow">OUR CORE VALUES</p>
  <h2 class="values-title display">The Perfect <span class="gold">Solution For<br>Your Space</span></h2>
  <div class="values-photo" role="img" aria-label="Photo of a bright, clean modern office with desk and shelving"></div>
  <div class="value" style="top:294px">
    <div class="ico"><svg viewBox="0 0 24 24" fill="none" stroke="#0a4ea3" stroke-width="1.5"><circle cx="12" cy="9" r="6"/><path d="M9 9l2 2 4-4M8 14l-2 7 6-3 6 3-2-7"/></svg></div>
    <h3>Be Real</h3><p>There are many variations of passages of Lorem Ipsum available, but the majority have suffered alteration.</p>
  </div>
  <div class="value" style="top:385px">
    <div class="ico"><svg viewBox="0 0 24 24" fill="none" stroke="#0a4ea3" stroke-width="1.5"><rect x="4" y="4" width="16" height="16" rx="2"/><path d="M8 12l3 3 5-6"/></svg></div>
    <h3>Do It Right</h3><p>There are many variations of passages of Lorem Ipsum available, but the majority have suffered alteration.</p>
  </div>
  <div class="value" style="top:475px">
    <div class="ico"><svg viewBox="0 0 24 24" fill="none" stroke="#0a4ea3" stroke-width="1.5"><circle cx="12" cy="12" r="8"/><path d="M8 14c1 2 7 2 8 0M9 9h.01M15 9h.01"/></svg></div>
    <h3>Have Fun</h3><p>There are many variations of passages of Lorem Ipsum available, but the majority have suffered alteration.</p>
  </div>
  <div class="value" style="top:566px">
    <div class="ico"><svg viewBox="0 0 24 24" fill="none" stroke="#0a4ea3" stroke-width="1.5"><path d="M5 12h14M13 6l6 6-6 6"/></svg></div>
    <h3>Make It Easy</h3><p>There are many variations of passages of Lorem Ipsum available, but the majority have suffered alteration.</p>
  </div>
  <a class="btn yellow" style="left:535px;top:675px;width:130px;height:30px" href="#quote">
    <svg viewBox="0 0 10 10" fill="#0b1f3a"><path d="M5 0l1 4 4 1-4 1-1 4-1-4-4-1 4-1z"/></svg>Get A Quote!<svg viewBox="0 0 10 10" fill="#0b1f3a"><path d="M5 0l1 4 4 1-4 1-1 4-1-4-4-1 4-1z"/></svg>
  </a>
</section>

<section class="services">
  <h2 class="services-title display">Our Company <span class="navy">Provide The Best</span><br>Cleaning Service</h2>
  <p class="services-intro">We are committed to delivering exceptional cleaning services that leave your spaces sparkling<br>clean and hygienic. Our professional team uses eco-friendly products to ensure a safe and healthy environment for you.</p>
  <article class="card" style="left:106px">
    <h3>Commercial<br>Cleaning</h3>
    <div class="ico"><svg viewBox="0 0 24 24" fill="none" stroke="#fff" stroke-width="1.5"><rect x="5" y="4" width="14" height="16"/><path d="M8 8h2M14 8h2M8 12h2M14 12h2M10 20v-4h4v4"/></svg></div>
    <p>There are many variations of passages of lorem ipsum available, but the majority have suffered alteration in some form, by injected humour...</p>
    <a class="go" href="#commercial"><svg viewBox="0 0 12 12" fill="none" stroke="#0a4ea3" stroke-width="1.5"><path d="M2 6h8M7 3l3 3-3 3"/></svg></a>
  </article>
  <article class="card" style="left:359px">
    <h3>Residential<br>Cleaning</h3>
    <div class="ico"><svg viewBox="0 0 24 24" fill="none" stroke="#fff" stroke-width="1.5"><path d="M3 11l9-7 9 7M6 9v11h12V9M10 20v-5h4v5"/></svg></div>
    <p>There are many variations of passages of lorem ipsum available, but the majority have suffered alteration in some form, by injected humour...</p>
    <a class="go" href="#residential"><svg viewBox="0 0 12 12" fill="none" stroke="#0a4ea3" stroke-width="1.5"><path d="M2 6h8M7 3l3 3-3 3"/></svg></a>
  </article>
  <article class="card" style="left:612px">
    <h3>Window<br>Cleaning</h3>
    <div class="ico"><svg viewBox="0 0 24 24" fill="none" stroke="#fff" stroke-width="1.5"><rect x="5" y="4" width="14" height="16"/><path d="M12 4v16M5 12h14"/></svg></div>
    <p>There are many variations of passages of lorem ipsum available, but the majority have suffered alteration in some form, by injected humour...</p>
    <a class="go" href="#window"><svg viewBox="0 0 12 12" fill="none" stroke="#0a4ea3" stroke-width="1.5"><path d="M2 6h8M7 3l3 3-3 3"/></svg></a>
  </article>
  <article class="card" style="left:865px">
    <h3>Steam<br>Cleaning</h3>
    <div class="ico"><svg viewBox="0 0 24 24" fill="none" stroke="#fff" stroke-width="1.5"><path d="M8 20h8l-1-9H9zM12 11V5M9 5h6"/></svg></div>
    <p>There are many variations of passages of lorem ipsum available, but the majority have suffered alteration in some form, by injected humour...</p>
    <a class="go" href="#steam"><svg viewBox="0 0 12 12" fill="none" stroke="#0a4ea3" stroke-width="1.5"><path d="M2 6h8M7 3l3 3-3 3"/></svg></a>
  </article>
  <div class="help" style="left:466px;top:474px">
    <svg viewBox="0 0 24 24" fill="none" stroke="#0a4ea3" stroke-width="1.6"><path d="M5 4l3 1 1 4-2 1a11 11 0 0 0 6 6l1-2 4 1 1 3-2 2C10 20 3 13 3 6z"/><circle cx="17" cy="6" r="4" fill="#f7c400" stroke="none"/></svg>
    <div><small>Need Help?</small><strong>0412 555 019</strong></div>
  </div>
  <a class="btn" style="left:604px;top:474px;width:127px;height:30px" href="#quote">
    <svg viewBox="0 0 10 10" fill="#fff"><path d="M5 0l1 4 4 1-4 1-1 4-1-4-4-1 4-1z"/></svg>Get A Quote<svg viewBox="0 0 10 10" fill="#fff"><path d="M5 0l1 4 4 1-4 1-1 4-1-4-4-1 4-1z"/></svg>
  </a>
</section>

<div class="marquee" aria-hidden="true"><span>COMMERCIAL</span><span>✦</span><span>RESIDENTIAL</span><span>✦</span><span>WINDOW</span><span>✦</span><span>STEAM</span></div>

<footer class="site-footer" role="img" aria-label="Dark navy photo of a clean interior behind the footer"></footer>

<section class="newsletter">
  <h2 class="display">Join Our <span class="gold">Newsletter</span><br>Stay Up to Date</h2>
  <div class="field">Enter your email...</div>
  <a class="btn yellow" style="left:507px;top:174px;width:105px;height:30px" href="#subscribe">
    <svg viewBox="0 0 10 10" fill="#0b1f3a"><path d="M5 0l1 4 4 1-4 1-1 4-1-4-4-1 4-1z"/></svg>Submit<svg viewBox="0 0 10 10" fill="#0b1f3a"><path d="M5 0l1 4 4 1-4 1-1 4-1-4-4-1 4-1z"/></svg>
  </a>
</section>

<div class="wordmark footer-mark"><i></i>Thornbury Cleaning</div>
<p class="foot-about">Join the 35 + local businesses and both State and National Government bodies that trust us to keep their buildings / facilities / Schools clean all year around.</p>

<h4 class="foot-h" style="left:488px">Contact us</h4>
<div class="foot-line" style="left:488px;top:2999px;font-family:'Barlow Condensed',sans-serif;font-size:19px;font-weight:700;color:var(--gold);align-items:center">
  <svg viewBox="0 0 12 12" fill="none" stroke="#f7c400" stroke-width="1.3"><path d="M2 1l2 .5.5 2.5-1 .5a6 6 0 0 0 3 3l.5-1 2.5.5.5 2-1 1C5 10 1 6 1 2z"/></svg>0412 555 019</div>
<div class="foot-line" style="left:488px;top:3034px">
  <svg viewBox="0 0 12 12" fill="#f7c400"><rect x="1" y="3" width="10" height="7" rx="1"/></svg>info@thornburycleaning-example.com.au</div>
<div class="foot-line" style="left:488px;top:3058px">
  <svg viewBox="0 0 12 12" fill="#f7c400"><path d="M6 0a4 4 0 0 0-4 4c0 3 4 8 4 8s4-5 4-8a4 4 0 0 0-4-4z"/></svg>18 Ferris Lane Sale Victoria<br>3850</div>

<h4 class="foot-h" style="left:725px">Quick links</h4>
<ul class="links"><li>Home</li><li>Commercial</li><li>Residential</li><li>Window Cleaning</li><li>Steam Cleaning</li><li>Areas</li><li>Contact Us</li></ul>

<h4 class="foot-h" style="left:868px">Working Time</h4>
<div class="hours">Monday – Friday: 9am – 5pm<br>Saturday: 10.00am - 6.00pm<br>Sunday: <span class="gold">Closed</span></div>
<div class="social" aria-label="Social profile"><i></i></div>

<div class="foot-rule"></div>
<p class="legal" style="left:200px">© 2025 <b>Thornbury Cleaning.</b> All Right Reserved</p>
<p class="legal" style="left:488px"><b>ABN:</b> 41 602 118 357 &nbsp;&nbsp; | &nbsp;&nbsp; <b>ACN:</b> 602 118 357</p>
<div class="cards" aria-label="Accepted payments"><span></span><span></span><span></span><span></span><span></span></div>

</body>
</html>
```